Real Estate For Sale Signage

I'm an independent agent in Lismore NSW Australia with high standards and looking for a catching 'For Sale'sign board.
I like classy, elegant, stylish and simple best.
My colours are red, white and black.
I don't have a logo or other font designs I need to stick to. I like the concept of a house or real estate design.
Before I created this project I played around on publisher and created the PDF attached. I'm not sold on it, but I don't mind the way the name has been layed out. Originally I had a white background with black & red font.
Fancy fonts for my name would be nice, but must not be busy.
Updates

Just wanted to advise that I have updated my brief and used the tools available to help get my ideas through.

Thank you for your work and time.

Kind regards
Marella

Industry/Entity Type

Real Estate

Requirements
Must have
• For Sale
Marella Quint Real Estate (must stand out)
0400 517 382 (must stand out)
17 Tallowood Street North Lismore
www.marellaquintrealestate.com.au

```html
<!DOCTYPE html>
<html lang="en">
<head>
<meta charset="utf-8">
<title>For Sale – Marella Quint Real Estate</title>
<link rel="stylesheet" href="https://fonts.googleapis.com/css2?family=Anton&family=Cinzel+Decorative:wght@400&family=Poiret+One&family=Montserrat:wght@600&display=swap">
<style>
  :root {
    --sale-red: #ee1c1c;
    --band-red: #f2070d;
    --blush: #f7c9c9;
    --rose: #f06a6d;
    --paper: #ffffff;
  }
  * { margin: 0; padding: 0; box-sizing: border-box; }
  html, body { width: 1200px; height: 800px; overflow: hidden; background: var(--paper); }
  .sign {
    position: relative;
    width: 1200px;
    height: 800px;
    background: var(--paper);
    overflow: hidden;
  }
  .sign__headline {
    position: absolute;
    top: 30px;
    left: 0;
    width: 100%;
    text-align: center;
    font-family: "Anton", "Impact", sans-serif;
    font-weight: 400;
    font-size: 206px;
    line-height: 1;
    letter-spacing: 6px;
    color: var(--sale-red);
    text-shadow: 2px 3px 4px rgba(120, 0, 0, 0.35);
    transform: scaleX(1.36);
    transform-origin: center top;
  }
  .sign__streetscape {
    position: absolute;
    top: 290px;
    left: 0;
    width: 1200px;
    height: 250px;
  }
  .sign__band {
    position: absolute;
    top: 528px;
    left: 0;
    width: 1200px;
    height: 272px;
    background: var(--band-red);
  }
  .sign__contact p {
    position: absolute;
    left: 0;
    width: 100%;
    text-align: center;
    color: var(--paper);
    line-height: 1;
    white-space: nowrap;
  }
  .agent-name {
    top: 548px;
    font-family: "Cinzel Decorative", "Georgia", serif;
    font-size: 80px;
    letter-spacing: 2px;
  }
  .agent-phone {
    top: 630px;
    font-family: "Poiret One", "Helvetica", sans-serif;
    font-size: 74px;
    letter-spacing: 6px;
    font-weight: 400;
  }
  .agent-address {
    top: 694px;
    font-family: "Montserrat", "Arial", sans-serif;
    font-weight: 600;
    font-size: 46px;
  }
  .agent-web {
    top: 742px;
    font-family: "Montserrat", "Arial", sans-serif;
    font-weight: 600;
    font-size: 51px;
  }
</style>
</head>
<body>
  <main class="sign">
    <h1 class="sign__headline">FOR SALE</h1>

    <svg class="sign__streetscape" viewBox="0 0 1200 250" preserveAspectRatio="none" role="img" aria-label="Red silhouette streetscape of heritage houses, a domed civic building and gabled homes, framed by flowing floral flourishes">
      <defs>
        <linearGradient id="streetscape-tone" x1="0" y1="0" x2="0" y2="1">
          <stop offset="0" stop-color="#ffffff"/>
          <stop offset="0.3" stop-color="#fdf0f0"/>
          <stop offset="0.55" stop-color="#f7c9c9"/>
          <stop offset="0.8" stop-color="#f06a6d"/>
          <stop offset="1" stop-color="#f2070d"/>
        </linearGradient>
      </defs>
      <rect x="0" y="0" width="1200" height="250" fill="url(#streetscape-tone)"/>
    </svg>

    <div class="sign__band"></div>

    <section class="sign__contact">
      <p class="agent-name">Marella Quint</p>
      <p class="agent-phone">0400 517 382</p>
      <p class="agent-address">17 Tallowood Street North Lismore</p>
      <p class="agent-web">www.marellaquintrealestate.com.au</p>
    </section>
  </main>
</body>
</html>
```